EL VARNO EXECUTIVE SERVICE BUSINESS CARDS. FAST

Need business card layout with round logo vs square logo

I have attached a mock up of the business card layout both front and back. I would like to change the square logo to the round logo. And change concierge services on the front of card to guest services. The two yellow highlight circles need to be changed. 1. Please make 1 flower all yellow 2. Please insert unique (use script font) between chief and experience. Use an up sweeping arrow and change to the teal color

Target Market(s)

Transportation

Industry/Entity Type

Transportation

Contact Information for Business Card

Logo large on one side and main business line such as Taxi or executive car service or louisville guest services

Font styles to use
Decorative
Script
Other font styles liked:
• See logo especially the A In the logo

Colors
FFF300
FFF600
FEFA6F
FFFEC7
FFFEE8
FFC000
F8CF3A
FAE287
FDF2CF
FEFAEE

Requirements
Must have
• Logo Cool clean sophisticated design. Phone number list of services.
Nice to have
• Love the black with teal design but instead of vertical, please run line horizontal with a yellow flower splash/dot like the design
Should not have
• Childish animation.

```html
<!DOCTYPE html>
<html lang="en">
<head>
<meta charset="utf-8">
<title>El Varno Executive Service – Business Cards</title>
<link rel="stylesheet" href="https://fonts.googleapis.com/css2?family=Source+Sans+3:wght@400;600&display=swap">
<style>
  :root {
    --stage: #1d1d1e;
    --card: #121011;
    --gold: #e2c262;
    --gold-light: #f6e6a6;
    --gold-deep: #c9a03e;
    --text-light: #f2f0ea;
  }
  * { margin: 0; padding: 0; box-sizing: border-box; }
  html, body {
    width: 1200px; height: 874px; overflow: hidden;
    background: var(--stage);
    font-family: "Source Sans 3", "Myriad Pro", sans-serif;
  }
  .canvas {
    position: relative; width: 1200px; height: 874px;
    display: flex; flex-direction: column; align-items: center; justify-content: center; gap: 36px;
  }
  .card {
    position: relative; width: 560px; height: 320px;
    background: var(--card); border-radius: 18px;
    box-shadow: 0 14px 30px rgba(0,0,0,.55);
    overflow: hidden;
  }
  /* Front */
  .front .rule {
    position: absolute; left: 0; top: 0; width: 560px; height: 320px;
  }
  .front .tagline {
    position: absolute; left: 0; right: 0; top: 236px;
    text-align: center; color: var(--gold);
    font-size: 15px; font-weight: 600; letter-spacing: .3px;
  }
  .emblem {
    position: absolute; display: flex; align-items: center; justify-content: center;
  }
  .emblem svg { position: absolute; inset: 0; }
  .emblem .name {
    position: relative; color: var(--gold);
    font-weight: 600; letter-spacing: 1px; text-align: center; line-height: 1;
  }
  .front .emblem { left: 210px; top: 78px; width: 140px; height: 140px; }
  .front .emblem .name { font-size: 21px; }
  /* Back */
  .back .emblem { left: 52px; top: 85px; width: 150px; height: 150px; }
  .back .emblem .name { font-size: 23px; }
  .details { position: absolute; left: 262px; top: 104px; }
  .services { list-style: none; color: var(--text-light); font-size: 13px; line-height: 1.25; }
  .services li::before { content: "•"; color: var(--gold); margin-right: 6px; }
  .contact { margin-top: 12px; color: var(--gold); }
  .contact .phone { font-size: 26px; font-weight: 600; line-height: 1.05; }
  .contact .line { font-size: 16px; line-height: 1.2; }
</style>
</head>
<body>
<main class="canvas">

  <section class="card front" aria-label="Card front">
    <svg class="rule" viewBox="0 0 560 320" aria-hidden="true">
      <defs>
        <linearGradient id="goldLine" x1="0" x2="1">
          <stop offset="0" stop-color="#c9a03e"/>
          <stop offset=".5" stop-color="#f6e6a6"/>
          <stop offset="1" stop-color="#c9a03e"/>
        </linearGradient>
      </defs>
      <line x1="62" y1="148" x2="498" y2="148" stroke="url(#goldLine)" stroke-width="2.5"/>
      <circle cx="52" cy="148" r="11" fill="var(--gold)" role="img" aria-label="Small flower accent"/>
      <circle cx="508" cy="148" r="11" fill="var(--gold)" role="img" aria-label="Small flower accent"/>
    </svg>
    <div class="emblem">
      <svg viewBox="0 0 140 140" aria-hidden="true">
        <circle cx="70" cy="70" r="68" fill="var(--card)" stroke="var(--gold)" stroke-width="4"/>
        <circle cx="70" cy="70" r="58" fill="none" stroke="var(--gold)" stroke-width="2"/>
      </svg>
      <span class="name">EL VARNO</span>
    </div>
    <p class="tagline">Taxi with 4 Specific Number</p>
  </section>

  <section class="card back" aria-label="Card back">
    <div class="emblem">
      <svg viewBox="0 0 150 150" aria-hidden="true">
        <circle cx="75" cy="75" r="72" fill="none" stroke="var(--gold)" stroke-width="4"/>
        <circle cx="75" cy="75" r="62" fill="none" stroke="var(--gold)" stroke-width="2"/>
      </svg>
      <span class="name">EL VARNO</span>
    </div>
    <div class="details">
      <ul class="services">
        <li>Praesent luptatum</li>
        <li>Nostrud exerci tation</li>
        <li>Ullamcorper suscipit lobortis</li>
        <li>Dignissim qui blandit</li>
      </ul>
      <div class="contact">
        <p class="phone">555.014.2280</p>
        <p class="line">info@elvarnoexec.com</p>
        <p class="line">www.elvarnoexec.com</p>
      </div>
    </div>
  </section>

</main>
</body>
</html>
```